Brookmere Osteopathy flyer

I want a clean clear DL flyer (but also want an A4 poster) promoting a new Osteopathic business in a semi rural area in Tasmania (Australia).
It can have pictures like the examples attached to show people what Osteopathy is (its like Chiropractic and physiotherapy).
I am the sole practioner and am male, so any pictures would be best to be a white male if possible.
I've attached some wording, you can use all, or none of it
I don't have a phone number for the business yet
info@brookmereosteopathy.example
www.brookmereosteopathy.example
Target Market(s)
Australians, from tradies, professionals, babies to retired people
Industry/Entity Type
Health
Look and feel

```html
<!DOCTYPE html>
<html lang="en">
<head>
<meta charset="utf-8">
<title>Brookmere Osteopathy – DL Flyer &amp; A4 Poster</title>
<link href="https://fonts.googleapis.com/css2?family=Montserrat:wght@300;400;500;600;700;800&display=swap" rel="stylesheet">
<style>
  :root{
    --orange:#f7923a;
    --blue:#1b8fd3;
    --blue-deep:#1478c2;
    --ink:#1f1f1f;
    --grey-title:#6b6b6b;
    --panel:#f1f2f4;
    --line:#f5b27a;
  }
  *{box-sizing:border-box;margin:0;padding:0}
  html,body{width:681px;height:1200px;overflow:hidden;background:#fff}
  body{position:relative;font-family:'Montserrat',sans-serif;color:var(--ink)}
  .sheet-title{position:absolute;left:0;width:681px;text-align:center;font-weight:300;font-size:23px;letter-spacing:1px;color:var(--grey-title)}
  .piece{position:absolute;overflow:hidden;background:#fff;outline:1px solid #d9d9d9}
  .abs{position:absolute}
  .photo{position:absolute}
  .brand-badge{position:absolute;border-radius:50%;background:#fff;display:flex;align-items:center;justify-content:center;text-align:center;font-weight:700;color:var(--blue);line-height:1.15}
  .headline{position:absolute;font-weight:800;text-transform:uppercase;line-height:1;text-align:center}
  .headline .o{color:var(--orange)} .headline .b{color:var(--blue)}
  .list{position:absolute;list-style:none}
  .list li{display:flex;align-items:center;border-bottom:.6px solid var(--line);font-weight:500;white-space:nowrap}
  .list li:last-child{border-bottom:none}
  .tick{flex:none;fill:var(--blue)}
  .pill{position:absolute;background:#fff;border-radius:999px;display:flex;align-items:center;justify-content:center;font-weight:700;color:var(--ink);white-space:nowrap}

  /* DL front */
  .dl-front{left:146px;top:119px;width:175px;height:371px}
  .dl-front .headline{left:0;width:175px;top:205px;font-size:13.6px;line-height:14px}
  .dl-front .list{left:17px;top:250px;width:146px}
  .dl-front .list li{height:12.3px;font-size:6.2px}
  .dl-front .list li .cell{display:flex;align-items:center}
  .dl-front .list li .cell:first-child{width:80px}
  .dl-front .tick{width:5.5px;height:5.5px;margin-right:3px}
  .dl-front .footer-bar{position:absolute;left:0;bottom:0;width:175px;height:19px;background:var(--orange);color:#fff;font-weight:700;font-size:8.6px;display:flex;align-items:center;justify-content:center;white-space:nowrap}

  /* DL back */
  .dl-back{left:360px;top:119px;width:175px;height:371px;background:var(--orange)}
  .dl-back .pitch{position:absolute;left:10px;width:155px;top:230px;color:#fff;font-weight:700;font-size:9.2px;line-height:11.2px;text-align:center}
  .dl-back .contact-band{position:absolute;left:0;bottom:0;width:175px;height:54px;background:linear-gradient(135deg,var(--blue-deep),var(--blue))}
  .dl-back .pill{left:12px;top:308px;width:151px;height:17px;font-size:7.8px}
  .dl-back .phone{position:absolute;left:0;width:175px;top:332px;text-align:center;color:#fff;font-weight:600;font-size:14px}
  .dl-back .small{position:absolute;left:0;width:175px;text-align:center;color:#fff;font-weight:400;font-size:6.3px;white-space:nowrap}

  /* A4 poster */
  .a4{left:156px;top:580px;width:370px;height:523px}
  .a4 .side-panel{position:absolute;left:200px;top:285px;width:170px;height:238px;background:var(--panel)}
  .a4 .headline{left:24px;top:299px;text-align:left;font-size:21.5px;line-height:21.6px}
  .a4 .tag{position:absolute;left:24px;top:363px;width:158px;height:23px;border-radius:999px;background:var(--blue);color:#fff;font-weight:800;font-size:17px;display:flex;align-items:center;justify-content:center;white-space:nowrap}
  .a4 .intro{position:absolute;left:24px;top:400px;width:168px;font-size:7px;line-height:9.4px;font-weight:400}
  .a4 .contact-block{position:absolute;left:0;top:454px;width:193px;height:69px;background:var(--orange);border-top-right-radius:19px}
  .a4 .pill{left:24px;top:441px;width:158px;height:17px;font-size:8.4px;border:1px solid var(--line)}
  .a4 .phone{position:absolute;left:24px;top:471px;color:#fff;font-weight:600;font-size:18px}
  .a4 .small{position:absolute;left:24px;color:#fff;font-weight:300;font-size:7.6px;white-space:nowrap}
  .a4 .list{left:214px;top:343px;width:148px}
  .a4 .list li{height:16.6px;font-size:7.1px}
  .a4 .tick{width:6.2px;height:6.2px;margin-right:3px}
</style>
</head>
<body>
<svg width="0" height="0" style="position:absolute">
  <symbol id="tick" viewBox="0 0 10 10"><circle cx="5" cy="5" r="5"/><path d="M2.7 5.2l1.6 1.6 3-3.3" fill="none" stroke="#fff" stroke-width="1.3" stroke-linecap="round" stroke-linejoin="round"/></symbol>
</svg>

<h2 class="sheet-title" style="top:49px">DL FLYER</h2>

<!-- DL flyer front -->
<section class="piece dl-front">
  <div class="photo" role="img" aria-label="Osteopath treating a patient's lower back" style="left:0;top:0;width:175px;height:115px;background:linear-gradient(170deg,#ecebe9 0%,#d8b8a3 35%,#2f3b5e 70%,#c59f8a 100%)"></div>
  <svg class="abs" style="left:0;top:125px" width="175" height="30" viewBox="0 0 175 30" role="img" aria-label="Stylised spine illustration">
    <path d="M0 28 C20 25 25 12 50 6 L55 20 C35 22 25 30 0 30Z" fill="var(--blue)"/>
    <path d="M128 14 C145 8 160 6 175 3 L175 12 C160 14 145 18 130 24Z" fill="var(--blue)"/>
  </svg>
  <div class="brand-badge" style="left:46px;top:116px;width:82px;height:82px;font-size:9px">Brookmere<br>Osteopathy</div>
  <h1 class="headline"><span class="o">Common reasons<br>people visit</span><br><span class="b">an osteopath</span></h1>
  <ul class="list">
    <li><span class="cell"><svg class="tick"><use href="#tick"/></svg>Back / neck pain</span><span class="cell"><svg class="tick"><use href="#tick"/></svg>Sciatica</span></li>
    <li><span class="cell"><svg class="tick"><use href="#tick"/></svg>Disc related issues</span><span class="cell"><svg class="tick"><use href="#tick"/></svg>Plantar fasciitis</span></li>
    <li><svg class="tick"><use href="#tick"/></svg>Joint and muscle pain</li>
    <li><svg class="tick"><use href="#tick"/></svg>Pregnancy-related discomfort</li>
    <li><svg class="tick"><use href="#tick"/></svg>Headaches / migraines</li>
    <li><svg class="tick"><use href="#tick"/></svg>Tendonitis / Bursitis</li>
    <li><svg class="tick"><use href="#tick"/></svg>Adhesive capsulitis (frozen shoulder)</li>
    <li><svg class="tick"><use href="#tick"/></svg>Tennis / Golfers elbow</li>
  </ul>
  <div class="footer-bar">brookmereosteopathy.example</div>
</section>

<!-- DL flyer back -->
<section class="piece dl-back">
  <div class="abs" style="left:0;top:0;width:175px;height:230px;background:#fff"></div>
  <div class="photo" role="img" aria-label="Practitioner gently treating a newborn baby's head" style="left:0;top:0;width:175px;height:90px;background:linear-gradient(180deg,#c9c7d9 0%,#d4b4a3 45%,#3f93cf 100%)"></div>
  <div class="photo" role="img" aria-label="Osteopath stretching a woman's shoulder on a treatment table" style="left:0;top:92px;width:175px;height:110px;background:linear-gradient(175deg,#eef0f2 0%,#c9ab9a 35%,#2a2a2e 55%,#e2e6ee 85%)"></div>
  <svg class="abs" style="left:0;top:186px" width="175" height="50" viewBox="0 0 175 50" role="img" aria-label="Stylised spine illustration">
    <path d="M0 22 C40 14 70 2 105 10 C135 16 155 6 175 2 L175 50 L0 50Z" fill="var(--orange)"/>
    <path d="M0 28 C12 26 18 18 30 14 C60 4 80 4 105 8 C135 13 155 4 175 0 L175 8 C155 12 135 22 105 18 C80 14 60 14 35 22 C20 26 12 32 0 32Z" fill="var(--blue)"/>
  </svg>
  <p class="pitch">Osteopaths use a combination of joint manipulation, targeted deep tissue massage and stretching to improve function, relieve pain and support the body’s ability to heal itself.</p>
  <div class="contact-band"></div>
  <div class="pill">brookmereosteopathy.example</div>
  <div class="phone">(03) 6100 2481</div>
  <div class="small" style="top:351px">42 Millbrook Road, Brookmere</div>
  <div class="small" style="top:359px">info@brookmereosteopathy.example</div>
</section>

<h2 class="sheet-title" style="top:536px">A4 POSTER</h2>

<!-- A4 poster -->
<section class="piece a4">
  <div class="photo" role="img" aria-label="Osteopath stretching a woman's arm and shoulder on a treatment table" style="left:0;top:0;width:370px;height:240px;background:linear-gradient(172deg,#eef0f2 0%,#e4e1df 20%,#c9a896 40%,#2b2b30 60%,#d6dbe3 85%,#ffffff 100%)"></div>
  <div class="side-panel"></div>
  <svg class="abs" style="left:0;top:230px" width="370" height="60" viewBox="0 0 370 60" role="img" aria-label="Stylised spine illustration">
    <path d="M0 56 C25 54 35 36 60 28 C90 16 120 10 150 8 L150 26 C120 28 95 34 70 44 C45 54 25 60 0 60Z" fill="var(--blue)"/>
    <path d="M345 16 C355 12 362 10 370 8 L370 28 C362 30 355 32 348 36Z" fill="var(--blue)"/>
  </svg>
  <div class="photo" role="img" aria-label="Newborn baby receiving gentle cranial treatment" style="left:139px;top:222px;width:80px;height:80px;border-radius:50%;background:linear-gradient(180deg,#c8c5d6 0%,#d4b3a2 50%,#3f93cf 100%)"></div>
  <div class="brand-badge" style="left:213px;top:208px;width:126px;height:126px;font-size:13px">Brookmere<br>Osteopathy</div>
  <h1 class="headline"><span class="o">Common<br>reasons<br>people visit</span></h1>
  <div class="tag">AN OSTEOPATH</div>
  <p class="intro">Osteopaths use a combination of joint manipulation, targeted deep tissue massage and stretching to improve function, relieve pain and support the body’s ability to heal itself.</p>
  <div class="contact-block"></div>
  <div class="pill">brookmereosteopathy.example</div>
  <div class="phone">(03) 6100 2481</div>
  <div class="small" style="top:498px">42 Millbrook Road, Brookmere</div>
  <div class="small" style="top:508px">info@brookmereosteopathy.example</div>
  <ul class="list">
    <li><svg class="tick"><use href="#tick"/></svg>Back / neck pain</li>
    <li><svg class="tick"><use href="#tick"/></svg>Sciatica</li>
    <li><svg class="tick"><use href="#tick"/></svg>Disc related issues</li>
    <li><svg class="tick"><use href="#tick"/></svg>Joint and muscle pain</li>
    <li><svg class="tick"><use href="#tick"/></svg>Pregnancy-related discomfort</li>
    <li><svg class="tick"><use href="#tick"/></svg>Plantar fasciitis</li>
    <li><svg class="tick"><use href="#tick"/></svg>Headaches / migraines</li>
    <li><svg class="tick"><use href="#tick"/></svg>Tendonitis / Bursitis</li>
    <li><svg class="tick"><use href="#tick"/></svg>Adhesive capsulitis (frozen shoulder)</li>
    <li><svg class="tick"><use href="#tick"/></svg>Tennis / Golfers elbow</li>
  </ul>
</section>
</body>
</html>
```